website design for small business consultancy - strategic research and writing

About the business
I am starting a new consultancy business called "Quill Harbor Consulting". I have asked for logo designs through Pixel Forum and am in the process of finalising these. I have a professional background and am an excellent and passionate writer and I want this professionalism conveyed through a modern, strong (confident) but simple, professional and elegant website. For SEO purposes, the services I will offer will include, but not be limited to, grants, submissions, proposals, strategic documents, complex correspondence, curriculum vitae and resumes, business cases, reports, training (grants and report writing). I will be based in Perth, Western Australia.

I would prefer the website be presented in black and white but I am not averse to colour, provided it's not gaudy. I want a header band across the top with the capacity to insert my logo (which I will send to the successful web builder) and the nature of the services "Strategic Research and Writing Services". I also want a net folio icon and a contact us button to the right (in the header).

I want a level one menu item underneath the header with the following menus - About (homepage), Services, Testimonials, and Contact (page to include a contact form).

I would like the following text to appear on the homepage as a highlight - like a drawcard for visitors to the site about my passion for what I do - "Lifting every idea into clear prose".

I want the capacity for a photo of me to be inserted on the About page.

I would like testimonials to feature distinctly, possibly in a box type format, either horizontally across the page or a couple or few in a row. There needs to be clear delineation of the person providing the testimonial and the testimonial itself.

Generally though I want a one column website that is accessible to those with disabilities. This is important to me as I believe all people should have access to website data.

I want the website to be responsive to tablets and mobile devices with high level SEO. One that is easy to add page headings to, and easy to amend and add plug ins. Maybe a wordpress site? The website must be compatible with Nimbo Webbing as I have paid for that.

Use of imagery is fine provided it is open source and relevant to the focus of the business.

Happy to send through further detail if required.

Thank you in anticipation. I have appreciated the work submitted to date.

I will insert the content (yet to be drafted)

Target Market(s)

Local government, private business, government

Contact Information for Business Card

Business card - I would like the logo on the front along with Strategic Research and Writing Services. I want the contact details on the back including: my name, role, email, mobile, web address, address.

I wouldn't mind a side panel on the rear in the colour of the business card with "Lifting every idea into clear prose" on it. Maybe with the text going up vertically. I can get the logo in black and white. I will upload the logo asap.

Coding

Number of Pages Required

Font styles to use
Serif
Sans Serif
Script

Requirements
Must have
• I want an elegant business card, professional but modern, that accords in branding to the website.
Should not have
• I do not want to use the red and black logo thanks. Either of the others is fine.

```html
<!DOCTYPE html>
<html lang="en">
<head>
<meta charset="utf-8">
<title>Quill Harbor Consulting</title>
<link href="https://fonts.googleapis.com/css2?family=Lato:wght@400;700;900&family=Open+Sans:ital,wght@0,400;0,600;0,700;1,400&display=swap" rel="stylesheet">
<style>
:root{
  --accent:#19aecd;
  --ink:#1c1c1c;
  --text:#555;
  --band:#ececec;
  --footer:#333333;
  --footer-line:#4a4a4a;
  --white:#fff;
  --star:#f4b400;
}
*{margin:0;padding:0;box-sizing:border-box}
html,body{width:1200px;height:4140px;overflow:hidden}
body{position:relative;font-family:"Open Sans",sans-serif;color:var(--text);background:var(--white)}
.abs{position:absolute}
h1,h2,h3,h4{font-family:"Lato",sans-serif;color:var(--ink)}
.photo{position:absolute}

/* header */
.brand{left:100px;top:26px;width:172px;text-align:center;white-space:nowrap}
.brand-name{font:900 21px/25px "Lato",sans-serif;color:var(--ink)}
.brand-tag{margin-top:4px;font:600 8.5px/11px "Open Sans",sans-serif;color:var(--text);letter-spacing:.2px}
.topline{top:14px;font-size:14px;color:var(--ink);display:flex;align-items:center;gap:20px;white-space:nowrap}
.topicon{width:34px;height:34px;border-radius:50%;background:var(--ink);display:flex;align-items:center;justify-content:center}
.nav{left:397px;top:68px;display:flex;gap:28px;font:700 15px "Open Sans",sans-serif;color:var(--ink)}
.nav .on{color:var(--accent)}
.folio{left:868px;top:57px;height:44px;padding:0 10px;border:2px solid #ddd;border-radius:22px;display:flex;align-items:center;font:700 11px "Open Sans",sans-serif;color:var(--ink);white-space:nowrap}
.cta{left:950px;top:58px;width:138px;height:40px;background:var(--accent);color:var(--white);font:700 14px/40px "Open Sans",sans-serif;text-align:center}

.hero{left:0;top:108px;width:1200px;height:541px;background:
  radial-gradient(ellipse 420px 380px at 760px 260px,rgba(40,44,50,.55),transparent 70%),
  radial-gradient(ellipse 300px 260px at 230px 240px,rgba(190,200,170,.35),transparent 70%),
  linear-gradient(100deg,#6d7276 0%,#9a9c99 38%,#4a5056 70%,#7d8388 100%)}
.hero-title{left:120px;top:325px;font:900 41px/46px "Lato",sans-serif;color:var(--white);text-transform:uppercase;letter-spacing:-.5px}

/* about */
.about-frame{left:121px;top:744px;width:393px;height:251px;border:2px solid var(--accent)}
.about-photo{left:111px;top:754px;width:393px;height:247px;background:
  radial-gradient(ellipse 160px 120px at 240px 120px,rgba(235,235,240,.7),transparent 70%),
  linear-gradient(135deg,#c9ccd0,#8e949b 55%,#4f545c)}
.about-title{left:599px;top:736px;font-size:40px;font-weight:700}
.about-text{left:599px;top:798px;width:489px;font-size:14px;line-height:28.3px;text-align:justify}
.btn{background:var(--accent);color:var(--white);font:700 14px "Open Sans",sans-serif;display:flex;align-items:center;justify-content:center;gap:7px}
.readmore{left:599px;top:1023px;width:140px;height:45px}

/* services */
.services{left:0;top:1165px;width:1200px;height:732px;background:var(--band)}
.center-title{left:0;width:1200px;text-align:center;font-size:40px;font-weight:700}
.services-intro{left:0;top:1283px;width:1200px;text-align:center;font-size:14px;line-height:29px;color:#444}
.svc-photo{top:1364px;width:394px;height:250px}
.svc-title{top:1643px;font:600 16px "Open Sans",sans-serif;color:var(--ink);letter-spacing:.3px}
.svc-text{top:1680px;width:360px;font-size:14px;line-height:28.5px;color:#444}
.learn{top:1813px;font:600 14px "Open Sans",sans-serif;color:var(--accent);display:flex;align-items:center;gap:7px}

/* testimonials */
.quote-box{top:2061px;width:309px;height:233px;border:2px solid var(--accent);text-align:center;padding-top:16px}
.quote-box p{font-style:italic;font-size:13px;line-height:24px;color:#555;padding:0 24px;margin-top:8px}
.stars{color:var(--star);font-size:14px;letter-spacing:2px;margin-top:6px}
.avatar{top:2259px;width:70px;height:70px;border-radius:50%;background:linear-gradient(160deg,#c59a7a,#6b4b3a);border:2px solid var(--white)}
.person{top:2347px;width:309px;text-align:center}
.person b{display:block;font:600 16px "Open Sans",sans-serif;color:var(--ink)}
.person span{font-size:13px;color:#555}
.dots{left:563px;top:2430px;display:flex;gap:4px}
.dots i{width:12px;height:12px;border-radius:50%;border:1px solid #999}
.dots i.on{background:var(--accent);border-color:var(--accent)}

/* steps */
.steps-photo{left:0;top:2538px;width:554px;height:590px;background:
  radial-gradient(ellipse 160px 260px at 110px 380px,rgba(40,48,64,.7),transparent 70%),
  radial-gradient(ellipse 180px 280px at 430px 390px,rgba(30,50,90,.75),transparent 70%),
  linear-gradient(180deg,#f2f4f6 0%,#dfe3e7 55%,#c5ccd4 100%)}
.steps-bg{left:554px;top:2538px;width:646px;height:590px;background:var(--band)}
.kicker{left:594px;top:2580px;font-size:13px;color:#444}
.steps-title{left:594px;top:2610px;font-size:30px;line-height:39px;font-weight:700}
.step{left:596px;width:500px;display:flex;gap:24px}
.step-icon{flex:none;width:52px;height:52px;border-radius:50%;background:var(--white);border:1px solid #ddd;display:flex;align-items:center;justify-content:center}
.step h4{font:600 17px "Open Sans",sans-serif;color:var(--ink);margin-bottom:6px}
.step p{font-size:14px;line-height:24px;color:#555}

/* contact cards */
.card{top:3224px;width:317px;height:150px;background:var(--white);box-shadow:0 0 6px rgba(0,0,0,.15);display:flex;align-items:center;padding-left:64px;gap:20px}
.card .ring{flex:none;width:66px;height:66px;border-radius:50%;border:2px solid var(--accent);display:flex;align-items:center;justify-content:center}
.card h4{font:400 20px "Open Sans",sans-serif;color:var(--ink);margin-bottom:4px}
.card p{font-size:14px;line-height:22px;color:#555}
.card p.mail{font-size:13px}
.map{left:111px;top:3374px;width:978px;height:301px;background:
  linear-gradient(75deg,transparent 52%,#a9d3ee 55%,#a9d3ee 60%,transparent 63%),
  linear-gradient(120deg,#e8ebee,#dde2e7 50%,#e6e9ec)}

/* footer */
.footer{left:0;top:3770px;width:1200px;height:370px;background:var(--footer)}
.fhead{top:3834px;font:700 16px "Lato",sans-serif;color:var(--white)}
.flinks{left:112px;top:3882px;font-size:14px;line-height:30px;color:var(--white);list-style:none}
.vline{top:3830px;width:1px;height:230px;background:var(--footer-line)}
.finfo{left:405px;top:3882px;font-size:14px;line-height:24px;color:var(--white)}
.finfo .row{display:flex;gap:8px;margin-bottom:10px}
.follow{font:700 14px "Lato",sans-serif;margin-top:4px;margin-bottom:8px}
.social{display:flex;align-items:center;gap:8px;font-size:12px}
.social i{width:34px;height:34px;border:1.5px solid #fff;border-radius:50%;display:inline-block}
.field{left:858px;width:230px;height:32px;border:1px solid #888;background:var(--white);font-size:13px;color:#444;line-height:30px;padding-left:14px}
.send{left:858px;top:4032px;width:83px;height:30px;font-size:14px}
.copy{left:0;top:4106px;width:1200px;text-align:center;font-size:13px;color:var(--white)}
</style>
</head>
<body>

<!-- header -->
<div class="abs brand">
  <div class="brand-name">QUILL HARBOR<br>CONSULTING</div>
  <div class="brand-tag">Strategic Research and Writing Services</div>
</div>
<div class="abs topline" style="left:479px">
  <span class="topicon"><svg width="14" height="12" viewBox="0 0 14 12"><rect x="1" y="1" width="12" height="10" fill="none" stroke="#fff" stroke-width="1.5"/><path d="M1 1l6 5 6-5" fill="none" stroke="#fff" stroke-width="1.5"/></svg></span>
  info@Quill Harbor Consulting
</div>
<div class="abs topline" style="left:779px">
  <span class="topicon"><svg width="14" height="12" viewBox="0 0 14 12"><rect x="1" y="1" width="12" height="10" fill="none" stroke="#fff" stroke-width="1.5"/><path d="M1 1l6 5 6-5" fill="none" stroke="#fff" stroke-width="1.5"/></svg></span>
  888 888 8888
</div>
<nav class="abs nav"><span class="on">Home</span><span>About us</span><span>Services</span><span>Testimonials</span><span>Contact</span></nav>
<div class="abs folio">net folio</div>
<div class="abs cta">CONTACT US</div>

<div class="photo hero" role="img" aria-label="Photo of professionals working at laptops in a bright office"></div>
<h1 class="abs hero-title">Lifting every idea<br>into clear prose</h1>

<!-- about -->
<div class="abs about-frame"></div>
<div class="photo about-photo" role="img" aria-label="Photo of a team meeting around a table with documents"></div>
<h2 class="abs about-title">ABOUT US</h2>
<p class="abs about-text">Am libero tempore, cum soluta nobis est eligendi optio cumque nihil impedit quo minus id quod maxime placeat facere possimus, omnis voluptas assumenda est, omnis dolor repellendus. Temporibus autem quibusdam et aut officiis debitis aut rerum necessitatibus saepe eveniet ut et voluptates repudiandae sint et molestiae non recusandae. Itaque earum rerum hic tenetur a sapiente delectus, ut aut reiciendis voluptatibus maiores alias consequatur</p>
<div class="abs btn readmore">READ MORE <svg width="13" height="13" viewBox="0 0 13 13"><circle cx="6.5" cy="6.5" r="5.5" fill="none" stroke="#fff" stroke-width="1.5"/><path d="M4 6.5h5M7 4.5l2 2-2 2" fill="none" stroke="#fff" stroke-width="1.4"/></svg></div>

<!-- services -->
<div class="abs services"></div>
<h2 class="abs center-title" style="top:1226px">OUR SERVICES</h2>
<p class="abs services-intro">Nam libero tempore, cum soluta nobis est eligendi optio cumque nihil impedit quo minus id<br>quod maxime placeat facere possimus,&nbsp; omnis voluptas assumenda est</p>

<div class="photo svc-photo" style="left:159px;background:radial-gradient(ellipse 120px 90px at 320px 60px,rgba(60,150,160,.6),transparent 70%),linear-gradient(160deg,#3a3d40,#505357 60%,#2d3033)" role="img" aria-label="Photo of hands typing on a laptop over printed charts"></div>
<h3 class="abs svc-title" style="left:180px">STRATEGIC RESEARCH</h3>
<p class="abs svc-text" style="left:180px">Nemo enim ipsam voluptatem voluptas aspernatur aut odit aut fugit, sed quia consequuntur dolores eos qui ratione voluptatem sequi nesciunt. Neque porro quisquam est, qui dolorem ipsum</p>
<div class="abs learn" style="left:180px">LEARN MORE <svg width="12" height="12" viewBox="0 0 13 13"><circle cx="6.5" cy="6.5" r="5.5" fill="none" stroke="#19aecd" stroke-width="1.5"/><path d="M4 6.5h5M7 4.5l2 2-2 2" fill="none" stroke="#19aecd" stroke-width="1.4"/></svg></div>

<div class="photo svc-photo" style="left:647px;background:radial-gradient(ellipse 140px 110px at 230px 110px,rgba(250,248,244,.8),transparent 70%),linear-gradient(135deg,#9c7248,#cfb490 50%,#ece6dc)" role="img" aria-label="Photo of a woman with a headset writing notes at a laptop"></div>
<h3 class="abs svc-title" style="left:668px">WRITING SERVICES</h3>
<p class="abs svc-text" style="left:668px">Nemo enim ipsam voluptatem voluptas aspernatur aut odit aut fugit, sed quia consequuntur dolores eos qui ratione voluptatem sequi nesciunt. Neque porro quisquam est, qui dolorem ipsum</p>
<div class="abs learn" style="left:668px">LEARN MORE <svg width="12" height="12" viewBox="0 0 13 13"><circle cx="6.5" cy="6.5" r="5.5" fill="none" stroke="#19aecd" stroke-width="1.5"/><path d="M4 6.5h5M7 4.5l2 2-2 2" fill="none" stroke="#19aecd" stroke-width="1.4"/></svg></div>

<!-- testimonials -->
<h2 class="abs center-title" style="top:1984px">TESTIMONIALS</h2>

<div class="abs quote-box" style="left:111px">
  <svg width="48" height="38" viewBox="0 0 48 38"><path d="M0 38V20C0 8 6 1 18 0v7c-6 1-9 5-9 11h9v20zM28 38V20c0-12 6-19 18-20v7c-6 1-9 5-9 11h9v20z" fill="#c4c4c4"/></svg>
  <p>Lorem ipsum dolor sit amet, consectetur adipiscing elit, sed do eiusmod tempor incididunt ut labore et dolore</p>
  <div class="stars">★★★★★</div>
</div>
<div class="abs quote-box" style="left:447px">
  <svg width="48" height="38" viewBox="0 0 48 38"><path d="M0 38V20C0 8 6 1 18 0v7c-6 1-9 5-9 11h9v20zM28 38V20c0-12 6-19 18-20v7c-6 1-9 5-9 11h9v20z" fill="#19aecd"/></svg>
  <p>Lorem ipsum dolor sit amet, consectetur adipiscing elit, sed do eiusmod tempor incididunt ut labore et dolore</p>
  <div class="stars">★★★★★</div>
</div>
<div class="abs quote-box" style="left:782px">
  <svg width="48" height="38" viewBox="0 0 48 38"><path d="M0 38V20C0 8 6 1 18 0v7c-6 1-9 5-9 11h9v20zM28 38V20c0-12 6-19 18-20v7c-6 1-9 5-9 11h9v20z" fill="#c4c4c4"/></svg>
  <p>Lorem ipsum dolor sit amet, consectetur adipiscing elit, sed do eiusmod tempor incididunt ut labore et dolore</p>
  <div class="stars">★★★★★</div>
</div>
<div class="photo avatar" style="left:230px;background:linear-gradient(160deg,#c9d0d8,#4f6075)" role="img" aria-label="Portrait photo of the client"></div>
<div class="photo avatar" style="left:566px" role="img" aria-label="Portrait photo of the client"></div>
<div class="photo avatar" style="left:901px;background:linear-gradient(160deg,#e2b48e,#7a4a2a)" role="img" aria-label="Portrait photo of the client"></div>
<div class="abs person" style="left:111px"><b>Tom Fairley</b><span>Sit Amet Consectotur</span></div>
<div class="abs person" style="left:447px"><b>Ada Lindqvist</b><span>Sit Amet Consectotur</span></div>
<div class="abs person" style="left:782px"><b>Mira Holt</b><span>Sit Amet Consectotur</span></div>
<div class="abs dots"><i></i><i></i><i class="on"></i><i></i><i></i></div>

<!-- steps -->
<div class="photo steps-photo" role="img" aria-label="Photo of two businessmen talking across a desk with a computer"></div>
<div class="abs steps-bg"></div>
<div class="abs kicker">Why Choose Us</div>
<h2 class="abs steps-title">4 STEPS TO MAKE OUR<br>SUCCESSFUL BUSINESS</h2>

<div class="abs step" style="top:2716px">
  <div class="step-icon"><svg width="24" height="24" viewBox="0 0 24 24" fill="none" stroke="#555" stroke-width="1.4"><rect x="3" y="4" width="18" height="14"/><path d="M7 14v-3M11 14V8M15 14v-5M3 21h18"/></svg></div>
  <div><h4>Analize Business</h4><p>Sed ut perspiciatis unde omnis iste natus error voluptatem accusantium doloremque laudantium,</p></div>
</div>
<div class="abs step" style="top:2813px">
  <div class="step-icon"><svg width="24" height="24" viewBox="0 0 24 24" fill="none" stroke="#555" stroke-width="1.4"><rect x="5" y="3" width="14" height="18"/><path d="M8 8h8M8 12h8M8 16h5"/></svg></div>
  <div><h4>Advice Business Plan</h4><p>Sed ut perspiciatis unde omnis iste natus error voluptatem accusantium doloremque laudantium,</p></div>
</div>
<div class="abs step" style="top:2911px">
  <div class="step-icon"><svg width="24" height="24" viewBox="0 0 24 24" fill="none" stroke="#555" stroke-width="1.4"><circle cx="12" cy="6" r="3"/><circle cx="5" cy="18" r="3"/><circle cx="19" cy="18" r="3"/><path d="M12 9v4M7 16l5-3 5 3"/></svg></div>
  <div><h4>Strategic Business Plan</h4><p>Sed ut perspiciatis unde omnis iste natus error voluptatem accusantium doloremque laudantium,</p></div>
</div>
<div class="abs step" style="top:3007px">
  <div class="step-icon"><svg width="24" height="24" viewBox="0 0 24 24" fill="none" stroke="#555" stroke-width="1.4"><path d="M3 21h18M6 18v-4M10 18v-7M14 18V8M18 18V4"/></svg></div>
  <div><h4>Results of Business Plan</h4><p>Sed ut perspiciatis unde omnis iste natus error voluptatem accusantium doloremque laudantium,</p></div>
</div>

<!-- contact -->
<div class="photo map" role="img" aria-label="Street map showing the office location"></div>
<div class="abs card" style="left:109px">
  <div class="ring"><svg width="22" height="22" viewBox="0 0 24 24"><path d="M6 2l4 4-2 3c1 3 4 6 7 7l3-2 4 4-3 4C10 22 2 14 2 5z" fill="none" stroke="#19aecd" stroke-width="1.8"/></svg></div>
  <div><h4>Phone</h4><p>888 888 8888</p></div>
</div>
<div class="abs card" style="left:440px">
  <div class="ring"><svg width="20" height="24" viewBox="0 0 20 24"><path d="M10 23s8-8 8-14A8 8 0 0 0 2 9c0 6 8 14 8 14z" fill="none" stroke="#19aecd" stroke-width="1.8"/><circle cx="10" cy="9" r="3" fill="#19aecd"/></svg></div>
  <div><h4>Address</h4><p>Neque porro&nbsp; est, qui<br>dolorem ipsum quia</p></div>
</div>
<div class="abs card" style="left:773px;padding-left:10px;gap:14px">
  <div class="ring"><svg width="24" height="18" viewBox="0 0 24 18"><rect x="1" y="1" width="22" height="16" fill="none" stroke="#19aecd" stroke-width="1.8"/><path d="M1 1l11 9 11-9" fill="none" stroke="#19aecd" stroke-width="1.8"/></svg></div>
  <div><h4>E- Mail</h4><p class="mail">info@quillharborconsulting.com</p></div>
</div>

<!-- footer -->
<div class="abs footer"></div>
<div class="abs fhead" style="left:112px">COMPANY</div>
<ul class="abs flinks"><li>Home</li><li>About Us</li><li>Services</li><li>Our Team</li><li>Testimonials</li><li>Contact Us</li></ul>
<div class="abs vline" style="left:294px"></div>
<div class="abs fhead" style="left:405px">CONTACT US</div>
<div class="abs finfo">
  <div class="row"><svg width="10" height="14" viewBox="0 0 10 14" style="margin-top:5px"><path d="M5 14S0 8 0 5a5 5 0 0 1 10 0c0 3-5 9-5 9z" fill="#fff"/></svg><span>At vero eos et accusamus<br>et iusto odio dignissimos</span></div>
  <div class="row"><svg width="12" height="12" viewBox="0 0 24 24" style="margin-top:6px"><path d="M6 2l4 4-2 3c1 3 4 6 7 7l3-2 4 4-3 4C10 22 2 14 2 5z" fill="#fff"/></svg><span>888 888 8888</span></div>
  <div class="row"><svg width="13" height="10" viewBox="0 0 24 18" style="margin-top:7px"><rect x="1" y="1" width="22" height="16" fill="none" stroke="#fff" stroke-width="2"/><path d="M1 1l11 9 11-9" fill="none" stroke="#fff" stroke-width="2"/></svg><span>info@Quill Harbor Consulting.com</span></div>
  <div class="follow">FOLLOW US</div>
  <div class="social"><i></i><span>net folio</span></div>
</div>
<div class="abs vline" style="left:749px"></div>
<div class="abs fhead" style="left:858px">GET IN TOUCH</div>
<div class="abs field" style="top:3889px">Enter Your Name</div>
<div class="abs field" style="top:3934px">Enter Email Address</div>
<div class="abs field" style="top:3979px">Enter Phone Number</div>
<div class="abs btn send">SEND</div>
<div class="abs copy">© 2019 Quill Harbor Consulting. All Rights Reserved</div>

</body>
</html>
```